Album art cover

Album art design concept, my band will be releasing a 11 song rock album in the next few Months. We will be using it as a CD cover, poster, online art cover, maybe even Vinyl. Working album titles are "Copper in the rain" (Preferred album title) or "A lantern under the tide". Anything abstract, painting-like design, or whatever type of design that comes to mind. Fonts are designers choice. Thank You

Target Market(s)

Music business

Colors

Designer to choose colors to be used in the design.

Requirements
Must have
• Our band logo
Nice to have
• Anything abstract, attractive painting type, maybe even some kind of a futuristic design.
Should not have
• Skulls, blood-like, scary designs, nudity, emo type of design

```html
<!DOCTYPE html>
<html lang="en">
<head>
<meta charset="utf-8">
<title>Copper in the rain — Album Cover</title>
<link rel="stylesheet" href="https://fonts.googleapis.com/css2?family=Raleway:wght@300;600&display=swap">
<style>
  :root {
    --navy-base: #0a1a33;
    --navy-deep: #061227;
    --navy-mid: #10274a;
    --navy-soft: #173358;
    --navy-stroke: #1d3c66;
    --ink-white: #f2f4f8;
  }
  html, body {
    margin: 0;
    padding: 0;
    width: 1200px;
    height: 1200px;
    overflow: hidden;
    background: var(--navy-base);
  }
  .album-cover {
    position: relative;
    width: 1200px;
    height: 1200px;
    overflow: hidden;
    font-family: "Raleway", "Helvetica Neue", Arial, sans-serif;
    color: var(--ink-white);
  }
  .painted-backdrop {
    position: absolute;
    inset: 0;
    background:
      radial-gradient(ellipse 38% 16% at 30% 14%, rgba(29, 60, 102, 0.75) 0%, transparent 70%),
      radial-gradient(ellipse 30% 12% at 72% 28%, rgba(29, 60, 102, 0.6) 0%, transparent 70%),
      radial-gradient(ellipse 42% 14% at 22% 42%, rgba(23, 51, 88, 0.7) 0%, transparent 72%),
      radial-gradient(ellipse 34% 11% at 66% 52%, rgba(23, 51, 88, 0.55) 0%, transparent 70%),
      radial-gradient(ellipse 40% 13% at 18% 66%, rgba(16, 39, 74, 0.8) 0%, transparent 72%),
      radial-gradient(ellipse 36% 12% at 46% 80%, rgba(16, 39, 74, 0.7) 0%, transparent 70%),
      radial-gradient(ellipse 30% 10% at 12% 90%, rgba(23, 51, 88, 0.5) 0%, transparent 70%),
      radial-gradient(ellipse 45% 35% at 85% 8%, rgba(6, 18, 39, 0.8) 0%, transparent 75%),
      linear-gradient(170deg, var(--navy-mid) 0%, var(--navy-base) 50%, var(--navy-deep) 100%);
  }
  .album-title {
    position: absolute;
    top: 20px;
    left: 0;
    right: 0;
    margin: 0;
    text-align: center;
    font-weight: 300;
    font-size: 36px;
    letter-spacing: 0.12em;
    text-transform: uppercase;
  }
  .band-name {
    position: absolute;
    top: 532px;
    right: 356px;
    margin: 0;
    text-align: right;
    font-weight: 600;
    font-size: 84px;
    line-height: 0.9;
    letter-spacing: 0.03em;
    text-transform: uppercase;
    color: var(--ink-white);
  }
  .band-name span { display: block; }
  .ornament-vine {
    position: absolute;
    left: 775px;
    top: 712px;
    width: 425px;
    height: 488px;
    background:
      radial-gradient(ellipse 40% 55% at 82% 55%, rgba(242, 244, 248, 0.85) 0%, rgba(242, 244, 248, 0.45) 50%, transparent 85%),
      radial-gradient(ellipse 45% 25% at 45% 22%, rgba(242, 244, 248, 0.45) 0%, transparent 80%),
      radial-gradient(ellipse 30% 30% at 20% 55%, rgba(242, 244, 248, 0.3) 0%, transparent 80%);
  }
  .album-subtitle {
    position: absolute;
    bottom: 16px;
    left: 0;
    right: 0;
    margin: 0;
    text-align: center;
    font-weight: 300;
    font-size: 36px;
    letter-spacing: 0.12em;
    text-transform: uppercase;
  }
</style>
</head>
<body>
  <main class="album-cover">
    <div class="painted-backdrop" role="img" aria-label="Abstract painted brushstroke texture in layered deep navy blues"></div>
    <h1 class="album-title">Copper in the rain</h1>
    <div class="ornament-vine" role="img" aria-label="White floral vine ornament with curling leaves and paint splashes rising from the lower right corner"></div>
    <h2 class="band-name"><span>Velvet</span><span>Harbor</span></h2>
    <p class="album-subtitle">A lantern under the tide</p>
  </main>
</body>
</html>
```